Sun Jubilee - Concert Poster

We need a poster for a concert involving 3 bands. Marmaduke, Auntie's Gumbo and Velveteen Ray. The event is called the Sun Jubilee. The poster will be a take away. We plan to print some to give out and some for advertising. Should be something people will want to put up on a wall. The poster should have a psychedelic "flavor", colorful.
Info. that needs to be on the poster: Sun Jubilee - Band Names - Pelham Brook's Music Hall - 4182 Route 17, Brightwater OR - $10 advance Tix - $12 at Door - for tickets www.pelhambrookmusic. - 21 and Over - March 21 2015 - Doors open at 7:00.

Industry/Entity Type

Event

```html
<!DOCTYPE html>
<html lang="en">
<head>
<meta charset="utf-8">
<title>Sun Jubilee – Concert Poster</title>
<link rel="stylesheet" href="https://fonts.googleapis.com/css2?family=Bungee&family=Cabin:wght@600;700&display=swap">
<style>
  :root {
    --backdrop: #e4e3e0;
    --poster-black: #0a0706;
    --stage-gold: #ffcf5a;
    --stage-amber: #f59a1c;
    --stage-ember: #b8490c;
    --stage-dark: #2a1206;
    --ink: #0c0a09;
    --accent-orange: #e8731c;
    --paper-white: #ffffff;
  }
  * { box-sizing: border-box; margin: 0; padding: 0; }
  html, body {
    width: 1200px;
    height: 1148px;
    overflow: hidden;
    background: var(--backdrop);
  }
  .poster {
    position: absolute;
    left: 226px;
    top: 24px;
    width: 748px;
    height: 1100px;
    background: var(--poster-black);
    overflow: hidden;
    font-family: "Cabin", "Gill Sans", sans-serif;
    color: var(--paper-white);
    text-align: center;
  }
  .stage-photo {
    position: absolute;
    left: 0; top: 0;
    width: 100%;
    height: 700px;
    background:
      radial-gradient(ellipse 70% 45% at 55% 42%, var(--stage-gold) 0%, rgba(255,207,90,0) 70%),
      linear-gradient(180deg, var(--stage-ember) 0%, var(--stage-amber) 35%, var(--stage-amber) 55%, var(--stage-dark) 82%, var(--poster-black) 100%);
  }
  .event-title {
    position: absolute;
    left: 0; right: 0; top: 0;
    font-family: "Bungee", "Impact", sans-serif;
    font-weight: 400;
    color: var(--ink);
    line-height: 1;
  }
  .event-title .title-main {
    display: block;
    position: absolute;
    left: 0; right: 0;
    top: 120px;
    font-size: 196px;
    letter-spacing: 4px;
  }
  .event-title .title-sub {
    display: block;
    position: absolute;
    left: 0; right: 0;
    top: 318px;
    font-size: 88px;
    letter-spacing: 2px;
  }
  .band-lineup {
    position: absolute;
    left: 0; right: 0;
    top: 440px;
    font-family: "Bungee", "Impact", sans-serif;
    font-size: 24px;
    color: var(--ink);
    letter-spacing: 0.5px;
    white-space: nowrap;
  }
  .band-lineup .divider {
    display: inline-block;
    width: 2px;
    height: 26px;
    background: var(--ink);
    margin: 0 10px;
    vertical-align: -4px;
  }
  .venue-name {
    position: absolute;
    left: 0; right: 0;
    top: 740px;
    font-family: "Cabin", "Gill Sans", sans-serif;
    font-weight: 700;
    font-size: 46px;
    color: var(--accent-orange);
    line-height: 1.1;
  }
  .event-details {
    position: absolute;
    left: 0; right: 0;
    top: 890px;
    font-weight: 700;
    font-size: 24px;
    line-height: 40px;
    letter-spacing: 0.5px;
    white-space: nowrap;
  }
  .event-details .address { font-size: 26px; }
  .event-details .pricing { color: var(--accent-orange); font-size: 26px; }
</style>
</head>
<body>
  <main class="poster">
    <div class="stage-photo" role="img" aria-label="Concert photograph: stage lights glowing orange over a cheering crowd silhouette"></div>

    <h1 class="event-title">
      <span class="title-main">SUN</span>
      <span class="title-sub">JUBILEE</span>
    </h1>

    <p class="band-lineup">
      MARMADUKE<span class="divider"></span>AUNTIE'S GUMBO<span class="divider"></span>VELVETEEN RAY
    </p>

    <p class="venue-name">Pelham Brook's<br>Music Hall</p>

    <div class="event-details">
      <p class="address">4182 ROUTE 17, BRIGHTWATER OR</p>
      <p class="pricing">$10 ADVANCE TIX - $12 AT DOOR</p>
      <p class="tickets">for tickets www.pelhambrookmusic.com</p>
      <p class="date">21 and Over - March 21 2015 - Doors open at 7:00.</p>
    </div>
  </main>
</body>
</html>
```